Kitchen Renovation in YOUR area

We need a template for a flyer that we can hand out in neighbourhoods when we're finished renovating a kitchen. Every neighbourhood, we'll swap out a before and after picture to personalize to that neighbourhood. These will be low print run flyers (30-50 each time). We're really hoping that they'll see *their* kitchen in the BEFORE section (since many houses in neighbourhoods are similar) and see what they're kitchen could look like in the AFTER section. So I want the BEFORE and AFTER photos to be easily swapped in and out on my end. I have lots of photos if needed.

Target Market(s)

Home owners looking to have their kitchen's renovated. This is typically in the 35-55 age range. Primarily women.

Colors

Designer to choose colors to be used in the design.

Requirements
Must have
• My logo, a before (0962) and an after (8281) that I can swap out as I go from neighborhood to neighborhood. All the other design elements can be permanent.
• My website address: BrightmoorBuilders.com
Nice to have
• A background of some kitchen work I've done (1171.jpg). I've also included some copy. That copy can change - that's just something I did up quickly. Use what you can and I can make changes later

```html
<!DOCTYPE html>
<html lang="en">
<head>
<meta charset="utf-8">
<title>Brightmoor Home Renovations – Kitchen Refacing Flyer</title>
<link href="https://fonts.googleapis.com/css2?family=Bebas+Neue&family=Open+Sans:ital,wght@0,400;0,600;0,700;1,400;1,600&family=Dancing+Script:wght@600&display=swap" rel="stylesheet">
<style>
  :root {
    --brand-blue: #1f6fc0;
    --brand-blue-dark: #145a9e;
    --brand-blue-light: #3a9be0;
    --panel-grey: #f1f1f1;
    --text-dark: #3d3d3d;
    --white: #ffffff;
    --overlay: rgba(40, 40, 40, 0.72);
    --photo-warm: #b9875a;
    --photo-steel: #8d8f91;
    --photo-white: #e8e6e2;
    --photo-grey: #9a9ea3;
  }
  * { margin: 0; padding: 0; box-sizing: border-box; }
  html, body { width: 974px; height: 1200px; overflow: hidden; background: #ffffff; }
  .flyer { position: relative; width: 974px; height: 1200px; background: var(--white); overflow: hidden; font-family: "Open Sans", Arial, sans-serif; color: var(--text-dark); }

  .hero-photo { position: absolute; left: 38px; top: 182px; width: 898px; height: 423px;
    background: linear-gradient(100deg, #4a4744 0%, #6b5a48 35%, var(--photo-steel) 55%, var(--photo-warm) 80%, #a9774a 100%); }

  .header-wave { position: absolute; left: 0; top: 0; width: 974px; height: 380px; }

  .brand-name { position: absolute; left: 50px; top: 60px; color: var(--white); font-weight: 600; line-height: 1; }
  .brand-name .brand-main { display: block; font-size: 56px; letter-spacing: -0.5px; }
  .brand-name .brand-sub { display: block; font-size: 26px; margin-top: 4px; }

  .tagline { position: absolute; right: 42px; top: 42px; color: var(--white); font-family: "Dancing Script", cursive; font-size: 31px; font-weight: 600; }

  .headline-box { position: absolute; left: 38px; top: 350px; width: 406px; height: 238px; background: var(--overlay); padding: 18px 18px 0 20px; }
  .headline { font-family: "Bebas Neue", Impact, sans-serif; color: var(--white); font-size: 52px; line-height: 56px; font-weight: 400; }
  .headline-sub { margin-top: 10px; color: var(--white); font-style: italic; font-weight: 600; font-size: 13.5px; line-height: 20px; }

  .benefits { position: absolute; left: 38px; top: 628px; width: 898px; height: 232px; background: var(--panel-grey); display: flex; padding: 12px 0; }
  .benefit { flex: 1; padding: 0 12px; text-align: center; }
  .benefit + .benefit { border-left: 2px dotted #b8b8b8; }
  .benefit-icon { width: 62px; height: 62px; margin: 2px auto 12px; display: block; }
  .benefit p { text-align: justify; font-size: 13.4px; line-height: 19px; }

  .before-after { position: absolute; left: 38px; top: 878px; width: 898px; height: 250px; display: flex; gap: 6px; }
  .ba-photo { position: relative; flex: 1; overflow: hidden; }
  .ba-photo.before { background: linear-gradient(180deg, var(--photo-white) 0%, #dcd8d2 50%, var(--photo-warm) 72%, #a8784c 100%); }
  .ba-photo.after { background: linear-gradient(180deg, #f0efed 0%, #d9d9d9 40%, #5d6166 60%, var(--photo-grey) 75%, #eeeeee 100%); }
  .ba-ribbon { position: absolute; left: -52px; top: 26px; width: 230px; height: 36px; background: var(--brand-blue); color: var(--white); transform: rotate(-30deg); text-align: center; font-size: 19px; line-height: 36px; letter-spacing: 1px; }

  .footer-wave { position: absolute; left: 0; top: 1040px; width: 974px; height: 160px; }
  .footer-call { position: absolute; left: 0; width: 974px; top: 1130px; text-align: center; color: var(--white); font-size: 23px; display: flex; justify-content: center; align-items: center; gap: 10px; }
  .footer-call svg { width: 22px; height: 22px; }
  .footer-web { position: absolute; left: 0; width: 974px; top: 1168px; text-align: center; color: var(--white); font-size: 18px; }
</style>
</head>
<body>
<div class="flyer">

  <div class="hero-photo" role="img" aria-label="Photo of a refaced kitchen with oak cabinets, stainless steel fridge and microwave"></div>

  <svg class="header-wave" viewBox="0 0 974 380" aria-hidden="true">
    <defs>
      <linearGradient id="headerBlue" x1="0" y1="0" x2="0" y2="1">
        <stop offset="0" stop-color="#145a9e"/>
        <stop offset="1" stop-color="#2a86d4"/>
      </linearGradient>
    </defs>
    <path d="M0,0 H974 V184 C720,200 360,250 0,372 Z" fill="#ffffff"/>
    <path d="M0,0 H974 V166 C720,178 360,222 0,344 Z" fill="url(#headerBlue)"/>
  </svg>

  <div class="brand-name">
    <span class="brand-main">Brightmoor</span>
    <span class="brand-sub">home renovations</span>
  </div>
  <div class="tagline">Kitchen Renovation in YOUR area!</div>

  <div class="headline-box">
    <h1 class="headline">Turn your kitchen<br>into your dream<br>kitchen by refacing!</h1>
    <p class="headline-sub">We’ve just completed a kitchen refacing in your area and the results are stunning. Take a look!</p>
  </div>

  <section class="benefits">
    <div class="benefit">
      <svg class="benefit-icon" viewBox="0 0 62 62" aria-hidden="true">
        <circle cx="31" cy="31" r="27" fill="none" stroke="#1f6fc0" stroke-width="5"/>
        <path d="M31 15 V32 H43" fill="none" stroke="#1f6fc0" stroke-width="5" stroke-linecap="round"/>
      </svg>
      <p>A kitchen refacing takes much less time, and costs up to 60% less than a full kitchen renovation. Get the kitchen you always dreamed of without all of the disruption of a full renovation.</p>
    </div>
    <div class="benefit">
      <svg class="benefit-icon" viewBox="0 0 62 62" aria-hidden="true">
        <rect x="6" y="4" width="24" height="54" fill="#1f6fc0"/>
        <rect x="32" y="4" width="24" height="54" fill="#1f6fc0"/>
        <rect x="10" y="8" width="16" height="46" fill="#ffffff"/>
        <rect x="36" y="8" width="16" height="46" fill="#ffffff"/>
        <rect x="24" y="28" width="3" height="8" fill="#1f6fc0"/>
        <rect x="35" y="28" width="3" height="8" fill="#1f6fc0"/>
      </svg>
      <p>Refacing is a complete kitchen facelift. Replace the doors (and the out-dated style!), trim, and panels and pick something new and fresh. Make any modifications you’d like (is it time to switch that junk cabinet into a pot-and-pan cabinet?).</p>
    </div>
    <div class="benefit">
      <svg class="benefit-icon" viewBox="0 0 62 62" aria-hidden="true">
        <rect x="8" y="34" width="9" height="24" fill="#1f6fc0"/>
        <rect x="21" y="40" width="9" height="18" fill="#1f6fc0"/>
        <rect x="34" y="44" width="9" height="14" fill="#1f6fc0"/>
        <rect x="47" y="48" width="9" height="10" fill="#1f6fc0"/>
        <path d="M4 6 L22 22 L30 16 L48 32" fill="none" stroke="#1f6fc0" stroke-width="4"/>
        <path d="M40 34 L54 37 L51 23 Z" fill="#1f6fc0"/>
      </svg>
      <p>Less mess (no need to empty cupboards), less cost (save up to 60% of a typical kitchen renovation), save time (a kitchen refacing typically takes only 3 days!)</p>
    </div>
  </section>

  <section class="before-after">
    <div class="ba-photo before" role="img" aria-label="Before photo: dated kitchen with oak lower cabinets and white uppers">
      <div class="ba-ribbon">BEFORE</div>
    </div>
    <div class="ba-photo after" role="img" aria-label="After photo: refaced kitchen with white cabinets, mosaic backsplash and granite island">
      <div class="ba-ribbon">AFTER</div>
    </div>
  </section>

  <svg class="footer-wave" viewBox="0 0 974 160" aria-hidden="true">
    <defs>
      <linearGradient id="footerBlue" x1="0" y1="0" x2="0" y2="1">
        <stop offset="0" stop-color="#2a86d4"/>
        <stop offset="1" stop-color="#145a9e"/>
      </linearGradient>
    </defs>
    <path d="M0,52 C320,88 680,60 974,12 V160 H0 Z" fill="#ffffff"/>
    <path d="M0,66 C320,100 680,74 974,26 V160 H0 Z" fill="#3a9be0"/>
    <path d="M0,74 C320,106 680,82 974,38 V160 H0 Z" fill="url(#footerBlue)"/>
  </svg>

  <div class="footer-call">
    <span>Call today for your FREE estimate!</span>
    <svg viewBox="0 0 24 24" aria-hidden="true">
      <circle cx="12" cy="12" r="10.5" fill="none" stroke="#ffffff" stroke-width="2"/>
      <path d="M8.2 6.5 L10 8.6 L9 10.3 C9.8 12 11.8 14 13.7 15 L15.4 14 L17.5 15.8 L16.3 17.6 C12 17.4 6.6 12 6.4 7.7 Z" fill="#ffffff"/>
    </svg>
    <span>555-014-2273</span>
  </div>
  <div class="footer-web">www.brightmoorbuilders.com</div>

</div>
</body>
</html>
```